dealcraftmentor.com - Podcast Guest Marketing E-Flyer PDF

Dear Designers:I am in need of an attractive and attention-getting layout and design for a three-page marketing flyer (commonly known as a media one sheet) that will be sent via e-mail, as PDF file, to various Podcast hosts to market me as a guest on their podcasts. I want the design of the document to "mirror" the design and branding on my parent dealcraftmentor.com website. I am providing ALL the edited and proofread copy and content - the designer just needs to create the design for this marketing document. I want an active PDF document and icons should be used for WorkLoop, Phone, E-mail , and website- with hyperlinks that connect accordingly. I need a fast turnaround.
Updates

Dear Designers - instead of using the photo in the project file of me speaking to the audience for the banner image - I thought it would be a better idea to make this marketing piece specific to Podcast Hosts. Therefore, an image such as the one in the link below would be good to use for a banner image. https://www.pixelvarnow.com/find?q=podcast+studio+photos&mode=img&ref=univ&id=Qm7TzRk2LwPa9XcNvB4eHyU8sDjF1gA5oE3iKtZ6bW0nMh&w=1377&h=804#pic=vrolapemxq3BcT:

Target Market(s)

This PDF document will be sent to 650 Podcast hosts in North America via a broadcast e-mail.

Font styles to use
Sans Serif

Colors
ec1f27
ffffff
000000
333333
9d9d9d

Requirements
Must have
• A three-page layout that is easy to navigate in PDF form.
• Proper font styles and sizes for key emphasis areas on the document/
• Consistent branding to mirror my dealcraftmentor.com parent website
• Must be easy for people to read
• Attention-getting design elements and layout
• Professional and sophisticated design
• Icons for contact information
Should not have
• Should not be cluttered and junky-looking.
• Should not use small font sizes that makes it difficult to read.
• If Podcast hosts are interested in having me as a guest - they will read the content as required on three-pages

```html
<!DOCTYPE html>
<html lang="en">
<head>
<meta charset="utf-8">
<title>Dealcraft Mentor – Podcast Guest One Sheet</title>
<link href="https://fonts.googleapis.com/css2?family=Oswald:wght@400;500;600&family=Roboto:wght@400;500;700&family=Open+Sans:wght@400;600;700&display=swap" rel="stylesheet">
<style>
:root{
  --red:#ec1f27;
  --white:#ffffff;
  --black:#000000;
  --charcoal:#333333;
  --grey:#9d9d9d;
  --mist:#e7e7e7;
  --backdrop:#ececec;
}
*{box-sizing:border-box;margin:0;padding:0}
html,body{width:1200px;height:1200px;overflow:hidden}
body{background:var(--backdrop);font-family:"Open Sans",sans-serif;color:var(--charcoal);position:relative}
.page{position:absolute;width:386px;height:546px;background:var(--white);overflow:hidden}
.page--intro{left:76px;top:40px}
.page--offer{left:722px;top:40px}
.page--praise{left:408px;top:622px}
.abs{position:absolute}
.body-copy{font-size:5.9px;line-height:1.32;text-align:justify;color:#444}
.section-title{font-family:"Roboto",sans-serif;font-weight:700;font-size:6.9px;color:var(--red);text-transform:uppercase;letter-spacing:.1px}
.section-title--dark{color:var(--charcoal)}
/* brand */
.brand{left:0;width:386px;top:18px;display:flex;justify-content:center;align-items:center;gap:5px}
.brand__mark{width:18px;height:18px;background:var(--red)}
.brand__name{font-family:"Open Sans",sans-serif;font-weight:600;font-size:17px;color:var(--charcoal);letter-spacing:-.3px}
/* hero */
.hero{left:0;top:58px;width:386px;height:206px;background:linear-gradient(120deg,#1d1f26 0%,#3b3f4c 45%,#6a3b2e 70%,#2a2c33 100%)}
.hero__studio{right:0;top:0;width:200px;height:162px;background:radial-gradient(circle at 60% 45%,#9a8d7e 0%,#57524c 35%,rgba(40,40,46,0) 75%)}
.hero__title{left:13px;top:16px;font-family:"Oswald",sans-serif;font-weight:600;font-size:19px;line-height:1.08;color:var(--white);letter-spacing:.2px}
.hero__title span{color:var(--red);display:block}
.hero__sub{left:15px;top:64px;font-family:"Oswald",sans-serif;font-weight:400;font-size:10px;color:var(--white);letter-spacing:.1px}
.hero__bar{left:0;top:220px;width:386px;height:44px;background:var(--red)}
.hero__pitch{left:122px;top:227px;width:252px;font-size:6.7px;line-height:1.35;color:var(--white);text-align:justify}
.portrait{left:14px;top:162px;width:100px;height:100px;border-radius:50%;background:radial-gradient(circle at 50% 40%,#d9d9d9,#6d6d6d 70%,#3a3a3a);border:2px solid var(--charcoal)}
.lead{left:0;top:264px;width:386px;height:70px;background:var(--mist)}
/* numbered reasons */
.reason{display:flex;gap:5px;margin-bottom:7px}
.reason__num{flex:0 0 10px;height:10px;background:var(--red);color:var(--white);font-family:"Roboto",sans-serif;font-weight:700;font-size:7.5px;line-height:10px;text-align:center}
.reason .body-copy{flex:1}
/* footer */
.footer{left:0;bottom:0;width:386px;height:26px;background:var(--charcoal);display:flex;align-items:center;justify-content:space-between;padding:0 14px;font-size:5.8px;color:var(--white)}
.footer__item{display:flex;align-items:center;gap:4px}
.footer__item svg{width:7px;height:7px}
/* page 2 */
.event-photo{left:0;top:0;width:386px;height:142px;background:linear-gradient(100deg,#1a1a1a 0%,#555 55%,#9a9a9a 80%,#3d3d3d 100%)}
.media-box{left:14px;top:290px;width:360px;height:85px;border:1px solid var(--grey);display:grid;grid-template-columns:1fr 1fr 1fr;grid-template-rows:1fr 1fr;align-items:center;justify-items:center;padding:6px 8px}
.media-box__name{font-family:"Roboto",sans-serif;font-weight:700;font-size:10px;color:var(--charcoal);white-space:nowrap}
.note{font-size:4.4px;color:#555}
/* page 3 */
.quote-box{border:1px solid var(--grey);border-top:none}
.quote-box::before{content:"";position:absolute;left:0;right:0;top:0;border-top:1px solid var(--grey);margin-left:22px}
.quote-open,.quote-close{position:absolute;font-family:"Oswald",sans-serif;font-size:34px;line-height:1;color:#c9c9c9}
.quote-open{left:-2px;top:-14px}
.quote-close{right:-2px;bottom:-22px}
.attribution{font-size:5.7px;line-height:1.35;font-weight:600;color:var(--black)}
.cta-button{left:14px;top:464px;width:133px;height:36px;background:linear-gradient(#f0393f,#c8141b);border-radius:6px;color:var(--white);font-family:"Roboto",sans-serif;font-weight:700;font-size:7.4px;text-align:center;padding-top:7px;text-decoration:none}
.cta-line{left:182px;top:469px;font-family:"Roboto",sans-serif;font-size:11.5px;color:var(--red);width:192px;text-align:right;line-height:1.3}
</style>
</head>
<body>

<section class="page page--intro">
  <div class="abs brand"><div class="brand__mark"></div><div class="brand__name">dealcraftmentor®</div></div>

  <div class="abs hero">
    <div class="abs hero__studio" role="img" aria-label="Studio microphone on a shock mount in front of blurred coloured lights"></div>
    <h1 class="abs hero__title">MEET DEALCRAFT MENTOR®<span>DANIEL R. VESKOVAR</span></h1>
    <p class="abs hero__sub">THE EXPERT YOU NEED AS A GUEST ON YOUR PODCAST</p>
  </div>
  <div class="abs hero__bar"></div>
  <p class="abs hero__pitch">Are you looking for a relevant and appealing topic and an engaging subject matter expert who can provide measurable value and life-changing tips to the listeners of your podcast?</p>
  <div class="abs portrait" role="img" aria-label="Portrait photo of the speaker in a suit"></div>

  <div class="abs lead"></div>
  <h2 class="abs section-title section-title--dark" style="left:14px;top:273px">Why negotiating and decision making should be topics on your podcast</h2>
  <p class="abs body-copy" style="left:14px;top:285px;width:358px">Regardless of your podcast theme – it's important to remember that your listeners are negotiating all the time – in their personal lives, social lives, and especially in their business lives. Negotiating is an essential life skill. Everyone can improve his or her negotiating skills, and Daniel is the expert who can provide the answers your people crave. Your podcast listeners will benefit from Daniel's proven, practical, and relevant negotiating strategies and tips that will improve results and outcomes in all types of personal and business negotiations.</p>

  <h2 class="abs section-title" style="left:14px;top:343px">Six reasons to book Daniel R. Veskovar as a guest on your podcast</h2>
  <div class="abs" style="left:14px;top:360px;width:171px">
    <div class="reason"><div class="reason__num">1</div><p class="body-copy">Daniel is a dynamic, thought-provoking, engaging, captivating, and entertaining speaker who will share some great personal stories to help your listeners better understand and relate to the topic of negotiating and decision-making dynamics. He will indeed challenge the "status quo."</p></div>
    <div class="reason"><div class="reason__num">2</div><p class="body-copy">Daniel is the founder of dealcraftmentor.com® and is an internationally recognized expert and highly rated speaker on the topics of negotiating and decision-making dynamics that affect negotiated outcomes. His versatility and commitment to proper preparation will ensure that his content is tailored to address the theme of your podcast and the needs of your listeners.</p></div>
    <div class="reason"><div class="reason__num">3</div><p class="body-copy">Daniel has personally trained over 50,000 people of all experience levels, across multiple industries, in 31 countries how to negotiate more effectively.</p></div>
  </div>
  <div class="abs" style="left:201px;top:360px;width:171px">
    <div class="reason"><div class="reason__num">4</div><p class="body-copy">His five-star-rated presentations and training programs have been delivered around the world to small and medium-sized businesses, Apex 500 corporations, and large industry, trade, and peer-to-peer associations such as Young Leaders' Network and Founders' Circle.</p></div>
    <div class="reason"><div class="reason__num">5</div><p class="body-copy">With formal training in broadcasting and media arts, Daniel provides 30 years of experience as a professional speaker who can provide your listeners with valuable insights, solutions, and answers to address listeners' challenges and questions.</p></div>
    <div class="reason"><div class="reason__num">6</div><p class="body-copy">Daniel is the creator of the best-selling Deal Master Toolkit Audio Learning Program designed to be an effective all-in-one learning solution that helps people improve their negotiating capabilities and skills. He is also the host of his soon-to-be-launched Podcast – Learn How to Close.</p></div>
  </div>

  <footer class="abs footer">
    <span class="footer__item"><svg viewBox="0 0 10 10"><path d="M2 1h2l1 2.5-1.3 1a5 5 0 0 0 2.8 2.8l1-1.3L10 7v2a1 1 0 0 1-1 1A9 9 0 0 1 0 2a1 1 0 0 1 1-1z" fill="#ec1f27"/></svg>555-204-7318</span>
    <span class="footer__item"><svg viewBox="0 0 10 10"><rect x="0" y="2" width="10" height="6.5" fill="#ec1f27"/><path d="M0 2l5 3.5L10 2" stroke="#333" stroke-width=".9" fill="none"/></svg>daniel@veskovar.com</span>
    <span class="footer__item"><svg viewBox="0 0 10 10"><circle cx="5" cy="5" r="4.3" fill="none" stroke="#ec1f27" stroke-width="1.2"/><path d="M.7 5h8.6M5 .7c-2.4 2.6-2.4 6 0 8.6M5 .7c2.4 2.6 2.4 6 0 8.6" stroke="#ec1f27" stroke-width=".8" fill="none"/></svg>www.dealcraftmentor.com</span>
    <span class="footer__item"><svg viewBox="0 0 10 10"><rect x="1" y="1" width="8" height="8" fill="#ec1f27"/></svg>workloop.com/in/danielveskovar</span>
  </footer>
</section>

<section class="page page--offer">
  <div class="abs event-photo" role="img" aria-label="Black and white photo of the speaker presenting to a seated audience"></div>

  <h2 class="abs section-title" style="left:14px;top:160px">Six reasons to book Daniel R. Veskovar as a guest on your podcast</h2>
  <p class="abs body-copy" style="left:14px;top:175px;width:358px">Most people are intimidated by the prospect and process of negotiating – and often view negotiating as an uncomfortable haggling and bargaining process that may involve confrontation, anxiety, and stress. If podcast listeners are like most people – then they probably are concerned about being taken advantage of – or that they are missing out on potential opportunities in their personal, social, and business negotiations.</p>
  <p class="abs body-copy" style="left:14px;top:214px;width:358px">To alleviate your listeners' concerns, Daniel will provide them with easy-to-understand negotiating strategies, tactics, phrases, and tips they can immediately apply – the moment the podcast episode ends. Your listeners will feel more confident when they are equipped with the powerful and beneficial strategies and techniques that will help them save/make money and arrive at better outcomes when negotiating with customers, clients, suppliers, contractors, financial institutions, retailers, co-workers, colleagues, and family members.</p>

  <h2 class="abs section-title" style="left:14px;top:262px">Daniel R. Veskovar in the media</h2>
  <p class="abs body-copy" style="left:14px;top:277px;width:358px">Daniel has appeared on radio programs, written articles or contributed to articles for the following media outlets:</p>
  <div class="abs media-box">
    <span class="media-box__name">The Harbor Ledger</span>
    <span class="media-box__name">Capital Markets Weekly</span>
    <span class="media-box__name">Sales Momentum</span>
    <span class="media-box__name" style="grid-column:1 / span 2">Venture Forum</span>
    <span class="media-box__name">Ledgerline</span>
  </div>

  <h2 class="abs section-title" style="left:14px;top:384px">Three ways you can profit from booking Daniel R. Veskovar on your podcast</h2>
  <p class="abs body-copy" style="left:14px;top:397px;width:358px">Upon mutual agreement, podcast hosts and listeners can have access to the following money-saving and profit-generating opportunities:</p>
  <div class="abs" style="left:14px;top:422px;width:358px">
    <div class="reason"><div class="reason__num">1</div><p class="body-copy">Podcast hosts will be provided with a specific promotional code to share with your listeners that will entitle them to receive a special one-time discount of $19.95US off the purchase of the MP3 download of the Deal Master Toolkit Audio Learning Program available on my online store. Complete download and purchase instructions will be provided to podcast</p></div>
    <div class="reason"><div class="reason__num">2</div><p class="body-copy">Podcast hosts will receive a 10% commission payable on the net sales dollar revenue generated from the sale of MP3 downloads of Daniel's Deal Master Toolkit Audio Learning Program.</p></div>
    <div class="reason"><div class="reason__num">3</div><p class="body-copy">Podcast hosts will receive a 10% referral fee for any corporation or association that books Daniel for a presentation, seminar, or learning workshop that directly results from my participation on your podcast</p></div>
  </div>
  <p class="abs note" style="left:14px;top:505px">Note: Discount and commission payments are subject to agreement to standard terms and conditions.</p>

  <footer class="abs footer">
    <span class="footer__item"><svg viewBox="0 0 10 10"><path d="M2 1h2l1 2.5-1.3 1a5 5 0 0 0 2.8 2.8l1-1.3L10 7v2a1 1 0 0 1-1 1A9 9 0 0 1 0 2a1 1 0 0 1 1-1z" fill="#ec1f27"/></svg>555-204-7318</span>
    <span class="footer__item"><svg viewBox="0 0 10 10"><rect x="0" y="2" width="10" height="6.5" fill="#ec1f27"/><path d="M0 2l5 3.5L10 2" stroke="#333" stroke-width=".9" fill="none"/></svg>daniel@veskovar.com</span>
    <span class="footer__item"><svg viewBox="0 0 10 10"><circle cx="5" cy="5" r="4.3" fill="none" stroke="#ec1f27" stroke-width="1.2"/><path d="M.7 5h8.6M5 .7c-2.4 2.6-2.4 6 0 8.6M5 .7c2.4 2.6 2.4 6 0 8.6" stroke="#ec1f27" stroke-width=".8" fill="none"/></svg>www.dealcraftmentor.com</span>
    <span class="footer__item"><svg viewBox="0 0 10 10"><rect x="1" y="1" width="8" height="8" fill="#ec1f27"/></svg>workloop.com/in/danielveskovar</span>
  </footer>
</section>

<section class="page page--praise">
  <h2 class="abs section-title" style="left:14px;top:26px">Testimonials: what some clients are saying about the Dealcraft Mentor®</h2>

  <div class="abs quote-box" style="left:14px;top:59px;width:360px;height:91px">
    <span class="quote-open">“</span><span class="quote-close">”</span>
    <p class="abs body-copy" style="left:15px;top:13px;width:330px">Daniel Veskovar did a terrific job on my podcast. His negotiating insights and tips were well received by my listeners, and he was an engaging, knowledgeable, and entertaining guest. Given my expertise in real estate, I thought I was a good negotiator until Daniel taught me a few new strategies and tips during the podcast. I would recommend Daniel to any podcast host he is a pro and his topics are relevant and can benefit everyone.</p>
    <p class="abs attribution" style="left:15px;top:56px">Carl Benning<br>Podcast Host<br>Property Builders Podcast, Austin, Texas</p>
  </div>

  <h2 class="abs section-title" style="left:14px;top:173px;width:360px;line-height:1.35">Below is a partial listing of testimonials from attendees at a Founders' Circle (FC) event provided by the RT Halvorsen, chapter learning chair:</h2>

  <div class="abs quote-box" style="left:14px;top:215px;width:167px;height:75px">
    <span class="quote-open">“</span><span class="quote-close">”</span>
    <p class="abs body-copy" style="left:15px;top:18px;width:140px">A very engaging, entertaining, and inspirational speaker who provided very useful information, strategies, and tips to apply to all my future negotiations</p>
  </div>
  <div class="abs quote-box" style="left:206px;top:215px;width:168px;height:75px">
    <span class="quote-open">“</span><span class="quote-close">”</span>
    <p class="abs body-copy" style="left:15px;top:18px;width:140px">Thank you to FC Western New York for booking this speaker! I learned some things that I can address immediately and a lot material that I need to practice. Great session!</p>
  </div>
  <div class="abs quote-box" style="left:14px;top:318px;width:167px;height:75px">
    <span class="quote-open">“</span><span class="quote-close">”</span>
    <p class="abs body-copy" style="left:15px;top:17px;width:140px">Daniel was an outstanding speaker on the topic of negotiating! He was one of my favorite speakers ever! Daniel was a real 'teacher' versus other typical speakers who spend two hours bragging or promoting their book</p>
  </div>
  <div class="abs quote-box" style="left:206px;top:318px;width:168px;height:75px">
    <span class="quote-open">“</span><span class="quote-close">”</span>
    <p class="abs body-copy" style="left:15px;top:17px;width:140px">Daniel was a very knowledgeable and well-prepared speaker who provided helpful tips and scripts throughout the entire presentation! I would love to learn more from this speaker</p>
  </div>

  <p class="abs attribution" style="left:14px;top:414px">RT Halvorsen, CEO and President<br>Northgate Records Group<br>Founders' Circle (FC) Western New York<br>Learning Chair</p>

  <a class="abs cta-button" href="https://www.dealcraftmentor.com">READ MORE TESTIMONIALS<br><svg width="10" height="11" viewBox="0 0 10 11" style="margin-top:3px"><path d="M3.5 6V1.5a.8.8 0 0 1 1.6 0V5l3 .7a1 1 0 0 1 .8 1.1L8.5 10H4L1.8 7.2a.8.8 0 0 1 1.2-1z" fill="none" stroke="#fff" stroke-width=".8"/></svg></a>
  <p class="abs cta-line">Book Dealcraft Mentor®<br>Daniel R. Veskovar for Your Podcast</p>

  <footer class="abs footer">
    <span class="footer__item"><svg viewBox="0 0 10 10"><path d="M2 1h2l1 2.5-1.3 1a5 5 0 0 0 2.8 2.8l1-1.3L10 7v2a1 1 0 0 1-1 1A9 9 0 0 1 0 2a1 1 0 0 1 1-1z" fill="#ec1f27"/></svg>555-204-7318</span>
    <span class="footer__item"><svg viewBox="0 0 10 10"><rect x="0" y="2" width="10" height="6.5" fill="#ec1f27"/><path d="M0 2l5 3.5L10 2" stroke="#333" stroke-width=".9" fill="none"/></svg>daniel@veskovar.com</span>
    <span class="footer__item"><svg viewBox="0 0 10 10"><circle cx="5" cy="5" r="4.3" fill="none" stroke="#ec1f27" stroke-width="1.2"/><path d="M.7 5h8.6M5 .7c-2.4 2.6-2.4 6 0 8.6M5 .7c2.4 2.6 2.4 6 0 8.6" stroke="#ec1f27" stroke-width=".8" fill="none"/></svg>www.dealcraftmentor.com</span>
    <span class="footer__item"><svg viewBox="0 0 10 10"><rect x="1" y="1" width="8" height="8" fill="#ec1f27"/></svg>workloop.com/in/danielveskovar</span>
  </footer>
</section>

</body>
</html>
```